Business cards for a naturopathic day clinic for stem cell therapy

We need a basic design for a day clinic, that offers stem cell therapies for Lyme therapy and other severe chronic illnesses.
Our name is "Haus solvaKrĂ¤ut", which can be translated into "Manor solvaHerb". We are a couple of naturopaths working along side physiotherapists and osteopaths, yoga teachers and massage therapists. I attached our logo.

```html
<!DOCTYPE html>
<html lang="en">
<head>
<meta charset="utf-8">
<title>Haus solvaKräut – Stationery</title>
<link rel="stylesheet" href="https://fonts.googleapis.com/css2?family=Source+Sans+3:wght@300;400;600&family=Arimo:wght@400;700&display=swap">
<style>
  :root {
    --backdrop: #e1e1e3;
    --paper: #f4f4f4;
    --green: #b3c15c;
    --taupe: #8b7d72;
    --ink: #1f1f1f;
    --ink-soft: #333;
    --signature-tint: #e3e4ee;
    --shadow: 2px 3px 4px rgba(0,0,0,.28);
  }
  * { box-sizing: border-box; margin: 0; padding: 0; }
  html, body { width: 1200px; height: 1056px; overflow: hidden; }
  body {
    position: relative;
    background: radial-gradient(ellipse at 50% 40%, #ececee 0%, var(--backdrop) 70%, #d8d8da 100%);
    font-family: "Source Sans 3", sans-serif;
    color: var(--ink);
  }
  .sheet { position: absolute; background: var(--paper); box-shadow: var(--shadow); overflow: hidden; }

  /* brand name: uppercase, single colour, single weight */
  .brand { display: flex; align-items: center; gap: 8px; font-family: "Source Sans 3", sans-serif; font-weight: 400; text-transform: uppercase; letter-spacing: .08em; color: var(--taupe); white-space: nowrap; }
  .brand-mark { background: var(--green); flex: none; }

  /* letterhead */
  .letterhead { left: 59px; top: 215px; width: 509px; height: 720px; }
  .letterhead .brand { position: absolute; left: 39px; top: 45px; font-size: 19px; }
  .letterhead .brand-mark { width: 14px; height: 14px; }
  .letterhead-contact { position: absolute; left: 286px; top: 45px; display: flex; font-size: 7.4px; line-height: 9.2px; color: var(--ink-soft); }
  .letterhead-contact .address { padding-right: 7px; border-right: 1px solid var(--green); }
  .letterhead-contact .reach { padding-left: 6px; }
  .accent { color: var(--green); }
  .strong { font-weight: 600; }
  .icon { display: inline-block; width: 6px; height: 6px; margin-right: 3px; vertical-align: -0.5px; }
  .letter { position: absolute; left: 86px; width: 393px; font-family: "Arimo", sans-serif; font-size: 7.5px; line-height: 10.3px; color: var(--ink); }
  .letter-date { top: 166px; }
  .letter-recipient { top: 186px; }
  .letter-salutation { top: 257px; font-weight: 700; }
  .letter-body { top: 289px; text-align: justify; }
  .letter-body p + p { margin-top: 10.3px; }
  .letter-closing { top: 515px; }
  .signature { position: absolute; left: 86px; top: 541px; width: 124px; height: 16px; background: var(--signature-tint); border-radius: 3px; }
  .letter-signoff { top: 568px; }

  /* business cards */
  .card { top: 120px; width: 134px; height: 206px; }
  .card-front { left: 627px; }
  .card-front .brand { position: absolute; left: 14px; top: 20px; font-size: 8px; gap: 4px; }
  .card-front .brand-mark { width: 6px; height: 6px; }
  .card-person { position: absolute; left: 14px; top: 106px; }
  .card-person .name { font-size: 7px; font-weight: 600; color: var(--green); }
  .card-person .role { font-size: 5.4px; color: var(--ink-soft); }
  .card-rule { position: absolute; left: 14px; top: 131px; width: 11px; height: 1px; background: var(--green); }
  .card-details { position: absolute; left: 14px; top: 141px; font-size: 5.3px; line-height: 7.2px; color: var(--ink-soft); }
  .card-details .reach { margin-top: 7px; }
  .card-details .icon { width: 4.5px; height: 4.5px; margin-right: 2px; }
  .card-back { left: 854px; background: var(--green); }
  .card-back .brand { position: absolute; left: 108px; top: 190px; transform: rotate(-90deg); transform-origin: 0 0; font-size: 13px; color: #fff; }

  /* envelopes */
  .envelope { left: 605px; width: 534px; }
  .envelope-front { top: 376px; height: 266px; }
  .envelope-front .brand { position: absolute; left: 43px; top: 32px; font-size: 17px; }
  .envelope-front .brand-mark { width: 13px; height: 13px; }
  .envelope-address { position: absolute; left: 80px; top: 71px; font-size: 7.6px; color: var(--ink-soft); }
  .envelope-back { top: 667px; height: 268px; }
  .envelope-flap { position: absolute; left: 0; top: 0; width: 100%; height: 86px; }
  .envelope-flap-url { position: absolute; left: 0; top: 36px; width: 100%; text-align: center; font-size: 8.6px; letter-spacing: 1px; color: #fff; }
</style>
</head>
<body>

<section class="sheet letterhead">
  <div class="brand"><span class="brand-mark"></span>Haus solvaKräut</div>
  <div class="letterhead-contact">
    <div class="address">
      <span class="accent">HAUS</span> <span class="strong">SOLVAKRÄUT</span><br>
      Lindenweg 7<br>
      64321 Tannbach
    </div>
    <div class="reach">
      <svg class="icon" viewBox="0 0 10 10"><path d="M2 1l2 2-1 1.5c.7 1.3 1.2 1.8 2.5 2.5L7 6l2 2-1.5 1.5C4.5 9 1 5.5.5 2.5z" fill="none" stroke="#b3c15c" stroke-width="1"/></svg>+49 6100-5550123<br>
      <svg class="icon" viewBox="0 0 10 10"><rect x=".5" y="2" width="9" height="6" fill="none" stroke="#b3c15c"/><path d="M.5 2L5 5.5 9.5 2" fill="none" stroke="#b3c15c"/></svg>jonas@haus-solvakraeut.de<br>
      <svg class="icon" viewBox="0 0 10 10"><circle cx="5" cy="5" r="4.3" fill="none" stroke="#b3c15c"/><path d="M.7 5h8.6M5 .7c-2.4 2.6-2.4 6 0 8.6M5 .7c2.4 2.6 2.4 6 0 8.6" fill="none" stroke="#b3c15c" stroke-width=".8"/></svg>www.haus-solvakraeut.de
    </div>
  </div>

  <p class="letter letter-date">December 11, 2021</p>
  <p class="letter letter-recipient">Mr. John Doe<br>President<br>AA Corporation<br>111 Street Name, Suite#<br>City, State, 12345</p>
  <p class="letter letter-salutation">Dear Mr. John,</p>
  <div class="letter letter-body">
    <p>Lorem ipsum dolor sit amet, consectetur adipiscing elit. Integer diam quam, egestas eu ultrices eu, suscipit ac sapien. Phasellus eu dui nisi. Nam et euismod diam, nec lobortis tortor. Donec et diam nulla. Aenean varius tincidunt convallis. Aliquam a tortor at lacus dictum aliquet. Nunc laoreet metus sapien, in scelerisque augue consectetur in.</p>
    <p>Fusce nec justo laoreet, egestas justo sed, aliquet sem. Pellentesque pharetra massa non orci bibendum semper. Pellentesque cursus eu lectus a consectetur. Nunc volutpat suscipit posuere. Vestibulum facilisis vel quam malesuada mattis. Nulla in mattis tellus. Maecenas tristique mauris vitae pharetra tincidunt. In ut ornare risus. Integer molestie vestibulum nisi, semper dapibus mi condimentum eu.</p>
    <p>Nullam sagittis elit libero, id fringilla est tincidunt eget. Donec in ipsum ultricies, consectetur quam vel, facilisis elit. Phasellus tincidunt congue risus vel luctus. Suspendisse ut mollis neque. Donec ornare orci in turpis vestibulum, in ultrices metus scelerisque. Pellentesque mattis mattis nunc, nec tincidunt lacus egestas id. Fusce facilisis sagittis neque sit amet vulputate. Aliquam ut eros lobortis tortor facilisis vehicula. Sed sed luctus leo, at laoreet sapien. Donec placerat adipiscing ligula non euismod. In lobortis pretium nisl id luctus.</p>
    <p>Integer gravida tincidunt nibh, scelerisque tincidunt turpis. Suspendisse potenti. Nunc hendrerit euismod lectus id elementum. Fusce vitae gravida velit, quis eleifend lectus. In imperdiet mauris eu dui viverra sagittis. Donec tempor dui diam, condimentum gravida lacus pretium a. Nullam fringilla augue quis arcu placerat scelerisque. Aliquam nec tincidunt augue, sit amet posuere ipsum.</p>
  </div>
  <p class="letter letter-closing">Sincerely Yours,</p>
  <div class="signature" role="img" aria-label="Handwritten signature of Jonas Eberhart"></div>
  <p class="letter letter-signoff">Jonas Eberhart<br>Founder</p>
</section>

<section class="sheet card card-front">
  <div class="brand"><span class="brand-mark"></span>Haus solvaKräut</div>
  <div class="card-person">
    <div class="name">Jonas Eberhart</div>
    <div class="role">Founder</div>
  </div>
  <div class="card-rule"></div>
  <div class="card-details">
    <div><span class="accent">HAUS</span> <span class="strong">SOLVAKRÄUT</span><br>Lindenweg 7<br>64321 Tannbach</div>
    <div class="reach">
      <svg class="icon" viewBox="0 0 10 10"><path d="M2 1l2 2-1 1.5c.7 1.3 1.2 1.8 2.5 2.5L7 6l2 2-1.5 1.5C4.5 9 1 5.5.5 2.5z" fill="none" stroke="#b3c15c" stroke-width="1"/></svg>+49 6100-5550123<br>
      <svg class="icon" viewBox="0 0 10 10"><rect x=".5" y="2" width="9" height="6" fill="none" stroke="#b3c15c"/><path d="M.5 2L5 5.5 9.5 2" fill="none" stroke="#b3c15c"/></svg>jonas@haus-solvakraeut.de<br>
      <svg class="icon" viewBox="0 0 10 10"><circle cx="5" cy="5" r="4.3" fill="none" stroke="#b3c15c"/><path d="M.7 5h8.6" stroke="#b3c15c"/></svg>www.haus-solvakraeut.de
    </div>
  </div>
</section>

<section class="sheet card card-back">
  <div class="brand">Haus solvaKräut</div>
</section>

<section class="sheet envelope envelope-front">
  <div class="brand"><span class="brand-mark"></span>Haus solvaKräut</div>
  <p class="envelope-address">Lindenweg 7, 64321 Tannbach</p>
</section>

<section class="sheet envelope envelope-back">
  <svg class="envelope-flap" viewBox="0 0 534 86" preserveAspectRatio="none" aria-hidden="true">
    <path d="M0 0H534L531 72Q530 86 516 86H18Q4 86 3 72Z" fill="#b3c15c"/>
  </svg>
  <p class="envelope-flap-url">www.haus-solvakraeut.de</p>
</section>

</body>
</html>
```